Marlow Summit Holdings, LLC

I need a new business card desperately.

Please update my business card. I am looking for a professional modern classy design like the Brightfen Partners card in the attachments.

Industry/Entity Type

Investment

Contact Information for Business Card

Colors

Designer to choose colors to be used in the design.

```html
<!DOCTYPE html>
<html lang="en">
<head>
<meta charset="utf-8">
<title>Marlow Summit Holdings, LLC — Business Card</title>
<link href="https://fonts.googleapis.com/css2?family=Lato:wght@400;700;900&display=swap" rel="stylesheet">
<style>
  :root {
    --backdrop: #2b2e33;
    --card-white: #ffffff;
    --card-black: #111214;
    --ink: #2a2a2c;
    --ink-soft: #3a3a3d;
    --accent-blue: #2f4f86;
    --paper-white: #f5f6f7;
  }
  * { margin: 0; padding: 0; box-sizing: border-box; }
  html, body {
    width: 1200px; height: 900px; overflow: hidden;
    background: var(--backdrop);
    font-family: "Lato", Arial, sans-serif;
  }
  .canvas {
    position: relative; width: 1200px; height: 900px;
  }
  .card {
    position: absolute; left: 300px;
    width: 600px; height: 343px;
    border-radius: 26px;
    box-shadow: 0 14px 30px rgba(0,0,0,0.35);
  }
  /* Front */
  .card-front { top: 90px; background: var(--card-white); color: var(--ink); }
  .holder-name {
    position: absolute; left: 48px; top: 42px;
    font-weight: 900; font-size: 24px; letter-spacing: 0.5px; text-transform: uppercase;
  }
  .holder-title {
    position: absolute; left: 48px; top: 74px;
    font-size: 13px; letter-spacing: 1px; text-transform: uppercase;
    color: var(--accent-blue);
  }
  .rule {
    position: absolute; left: 48px; width: 40px; height: 3px;
    background: var(--accent-blue); border-radius: 2px;
  }
  .rule-one { top: 108px; }
  .rule-two { top: 200px; }
  .contact-line {
    position: absolute; left: 48px;
    display: flex; align-items: center; gap: 12px;
    font-size: 15px; color: var(--ink-soft);
  }
  .contact-line svg { width: 14px; height: 14px; fill: var(--accent-blue); flex: none; }
  .line-email { top: 130px; }
  .line-phone { top: 162px; }
  .line-address { top: 222px; }
  .brand-front {
    position: absolute; right: 44px; bottom: 44px;
    display: flex; align-items: center; gap: 12px;
  }
  .brand-mark { width: 18px; height: 18px; background: var(--accent-blue); flex: none; }
  .brand-name {
    font-weight: 900; font-size: 20px; letter-spacing: 1px;
    text-transform: uppercase; color: var(--ink);
  }
  /* Back */
  .card-back {
    top: 467px; background: var(--card-black);
    display: flex; align-items: center; justify-content: center;
  }
  .card-back .brand-name { color: var(--paper-white); font-size: 26px; }
  .card-back .brand-mark { width: 22px; height: 22px; }
</style>
</head>
<body>
<main class="canvas">
  <section class="card card-front" aria-label="Business card front">
    <div class="holder-name">Elena R. Marlow</div>
    <div class="holder-title">Managing Partner</div>
    <div class="rule rule-one"></div>
    <div class="contact-line line-email">
      <svg viewBox="0 0 16 16" aria-hidden="true"><path d="M1 3h14v10H1z M1 3l7 6 7-6" fill="none" stroke="currentColor"/><path d="M1 3h14L8 9z"/><rect x="1" y="4" width="14" height="9" fill="none" stroke="#2f4f86" stroke-width="1.4"/></svg>
      <span>emarlow@marlowsummit.com</span>
    </div>
    <div class="contact-line line-phone">
      <svg viewBox="0 0 16 16" aria-hidden="true"><path d="M4 1l3 3-2 2c1 2 3 4 5 5l2-2 3 3-2 3C7 15 1 9 1 3z"/></svg>
      <span>512.555.0148</span>
    </div>
    <div class="rule rule-two"></div>
    <div class="contact-line line-address">
      <svg viewBox="0 0 16 16" aria-hidden="true"><path d="M8 0a5 5 0 0 0-5 5c0 4 5 11 5 11s5-7 5-11a5 5 0 0 0-5-5zm0 7a2 2 0 1 1 0-4 2 2 0 0 1 0 4z"/></svg>
      <span>2207 Ridgeline Ave., Suite 310, Austin, Texas 78731</span>
    </div>
    <div class="brand-front">
      <span class="brand-mark"></span>
      <span class="brand-name">Marlow Summit Holdings, LLC</span>
    </div>
  </section>

  <section class="card card-back" aria-label="Business card back">
    <div class="brand-front" style="position:static;">
      <span class="brand-mark"></span>
      <span class="brand-name">Marlow Summit Holdings, LLC</span>
    </div>
  </section>
</main>
</body>
</html>
```